Real Estate Website

Brackwell Realty will primarily be a residential rental and sales business.

Sales - Current properties - sold properties
Rentals - current properties - leased properties
Insights - Blog - Suburb profile
About us - Our agents
Working with us - rental/Sales

Here is a site that i like. Dont require video in the background.
https://www.quenbydom.com.au/
Scaled down version of this would be great. I like the landing page where it focuses on the client being vendor/landlord - not the buyers and sellers

Please make a banner on the home page that says 'request a free appraisal' with a button saying 'click here'.

I've attached some branding logos etc.
Brand colour is #f6ecd7 but using a white or black as the main of the website is fine.

```html
<!DOCTYPE html>
<html lang="en">
<head>
<meta charset="utf-8">
<title>Brackwell Realty</title>
<link href="https://fonts.googleapis.com/css2?family=Mulish:wght@400;600;700&family=Lato:wght@300;400;700&display=swap" rel="stylesheet">
<style>
:root{
  --ink:#1c1c1c;
  --charcoal:#333333;
  --heading:#3d3d3d;
  --text:#555555;
  --brand:#f6ecd7;
  --beige-panel:#efe4d2;
  --dark-panel:#3c3b3a;
  --footer:#0a0a0a;
  --white:#ffffff;
}
*{box-sizing:border-box;margin:0;padding:0}
html,body{width:1200px;height:3257px;overflow:hidden}
body{position:relative;background:var(--white);font-family:'Lato',sans-serif;color:var(--text)}
.abs{position:absolute}

.site-header{position:absolute;left:0;top:0;width:1200px;height:140px;background:var(--white);border-bottom:1px solid #e6e6e6}
.brand{position:absolute;left:111px;top:36px;width:252px;text-align:center;font-family:'Mulish',sans-serif;font-weight:600;color:var(--ink);line-height:1}
.brand .brand-name{font-size:36px;letter-spacing:3px;display:block}
.brand .brand-sub{font-size:28px;letter-spacing:6px;display:block;margin-top:6px}
.main-nav{position:absolute;top:64px;font-family:'Mulish',sans-serif;font-size:15px;font-weight:600;color:var(--charcoal);letter-spacing:.3px}

.hero{position:absolute;left:0;top:140px;width:1200px;height:688px;background:linear-gradient(180deg,#d8c8b4 0%,#c9b49b 35%,#8c8a5a 65%,#6f7a43 100%)}
.hero-title{position:absolute;left:109px;top:365px;font-family:'Mulish',sans-serif;font-weight:700;font-size:56px;line-height:66px;color:var(--white);letter-spacing:.5px}
.btn-outline-light{position:absolute;left:111px;top:518px;width:181px;height:60px;border:2px solid var(--white);border-radius:30px;color:var(--white);font-family:'Mulish',sans-serif;font-weight:600;font-size:20px;display:flex;align-items:center;justify-content:center}

.section-title{position:absolute;left:0;width:1200px;text-align:center;font-family:'Mulish',sans-serif;font-weight:600;font-size:42px;color:var(--heading);letter-spacing:.5px}
.title-rule{position:absolute;left:576px;width:48px;height:3px;background:#eddcc0}

.about-copy{position:absolute;left:226px;width:748px;text-align:center;font-size:16.5px;line-height:33.5px;color:var(--text)}
.btn-dark{position:absolute;background:var(--charcoal);color:var(--white);border-radius:34px;font-family:'Mulish',sans-serif;font-weight:600;display:flex;align-items:center;justify-content:center}

.services{position:absolute;left:0;top:1434px;width:1200px;height:530px}
.service-icon{position:absolute;width:128px;height:128px;border-radius:50%;background:var(--white);border:2px solid #d9d2c8;display:flex;align-items:center;justify-content:center}
.service-title{position:absolute;width:440px;text-align:center;font-family:'Mulish',sans-serif;font-size:27px;font-weight:600}
.service-copy{position:absolute;width:424px;text-align:center;font-size:17px;line-height:25.8px}
.btn-pill{position:absolute;width:155px;height:52px;border-radius:26px;display:flex;align-items:center;justify-content:center;font-family:'Mulish',sans-serif;font-weight:700;font-size:15px}

.post-card{position:absolute;top:2133px;width:473px;height:280px;border:2px solid #dedede;background:var(--white)}
.post-photo{position:absolute;left:0;top:0;width:208px;height:276px}
.post-body{position:absolute;left:236px;top:26px;width:218px}
.post-title{font-family:'Mulish',sans-serif;font-weight:600;font-size:15px;line-height:24px;color:var(--heading)}
.post-meta{margin-top:10px;font-size:11.5px;color:#8a8a8a;display:flex;align-items:center;gap:6px}
.post-excerpt{margin-top:16px;font-size:13.5px;line-height:24px;color:#777;text-align:justify}

.working{position:absolute;left:0;top:2512px;width:1200px;height:365px;background:linear-gradient(100deg,#e7dcd3 0%,#d8c9bf 50%,#cdbcb1 100%)}
.working-visual{position:absolute;left:760px;top:0;width:440px;height:365px;background:linear-gradient(160deg,#b9b6b6 0%,#8e8d8f 45%,#cbb6a6 100%)}
.working-title{position:absolute;left:148px;top:82px;font-family:'Mulish',sans-serif;font-weight:600;font-size:37px;color:#4d4d4d;letter-spacing:.5px}
.working-copy{position:absolute;left:146px;top:146px;width:560px;font-size:18px;line-height:33px;color:#5c5c5c}
.btn-cream{position:absolute;left:147px;top:233px;width:184px;height:58px;border-radius:29px;background:#f8efe2;border:2px solid #d8c8b2;color:#4d4d4d;font-family:'Mulish',sans-serif;font-weight:600;font-size:18px;display:flex;align-items:center;justify-content:center}

.site-footer{position:absolute;left:0;top:2877px;width:1200px;height:380px;background:var(--footer);color:var(--white)}
.footer-brand{position:absolute;left:124px;top:110px;width:300px;text-align:center;font-family:'Mulish',sans-serif;font-weight:600;line-height:1}
.footer-brand .brand-name{font-size:44px;letter-spacing:3px;display:block}
.footer-brand .brand-sub{font-size:33px;letter-spacing:7px;display:block;margin-top:6px}
.footer-heading{position:absolute;top:70px;font-family:'Mulish',sans-serif;font-weight:600;font-size:18px;letter-spacing:.3px}
.footer-menu{position:absolute;left:480px;top:109px;list-style:none;font-family:'Mulish',sans-serif;font-size:12.5px;line-height:24px}
.footer-item{position:absolute;display:flex;align-items:center;gap:12px;font-family:'Mulish',sans-serif;font-size:12.5px;line-height:17px}
.footer-dot{width:24px;height:24px;border-radius:50%;background:var(--white);display:flex;align-items:center;justify-content:center;flex-shrink:0}
.footer-rule{position:absolute;left:111px;top:303px;width:977px;height:1px;background:#3a3a3a}
.copyright{position:absolute;left:0;top:333px;width:1200px;text-align:center;font-family:'Mulish',sans-serif;font-size:13px}
</style>
</head>
<body>

<header class="site-header">
  <div class="brand"><span class="brand-name">BRACKWELL</span><span class="brand-sub">REALTY</span></div>
  <nav>
    <span class="main-nav" style="left:451px">HOME</span>
    <span class="main-nav" style="left:537px">SALES</span>
    <span class="main-nav" style="left:623px">RENTALS</span>
    <span class="main-nav" style="left:729px">INSIGHTS</span>
    <span class="main-nav" style="left:838px">ABOUT US</span>
    <span class="main-nav" style="left:954px">WORKING WITH US</span>
  </nav>
</header>

<section class="hero" role="img" aria-label="Photo of a couple standing in a grassy field looking at a two-storey house at sunset">
  <h1 class="hero-title">REQUEST A<br>FREE APPRAISAL</h1>
  <span class="btn-outline-light">CLICK HERE</span>
</section>

<section class="about">
  <h2 class="section-title" style="top:872px">ABOUT US</h2>
  <div class="title-rule" style="top:937px"></div>
  <p class="about-copy" style="top:962px">It is a long established fact that a reader will be distracted by the readable content of a page when looking at its layout. The point of using Lorem Ipsum is that it has a more-or-less normal distribution of letters, as opposed to using 'Content here, content here', making it look like readable English. Many desktop publishing packages and web page editors now use Lorem Ipsum as their default model text, and a search for 'lorem ipsum' will uncover many web sites still in their infancy.</p>
  <p class="about-copy" style="top:1163px">Contrary to popular belief, Lorem Ipsum is not simply random text. It has roots in a piece of classical Latin literature from 45 BC, making it over 2000 years old. Edwin Harrowgate, a Latin professor at &nbsp;up one of the more obscure Latin words, consectetur,</p>
  <span class="btn-dark" style="left:490px;top:1296px;width:219px;height:66px;font-size:19px">LEARN MORE</span>
</section>

<section class="services">
  <svg class="abs" style="left:0;top:0" width="1200" height="530" viewBox="0 0 1200 530">
    <polygon points="0,38 598,38 632,530 0,530" fill="#efe4d2" role="img" aria-label="Faded photo of an agent meeting clients at a table"/>
    <polygon points="597,0 1200,0 1200,492 629,492" fill="#3c3b3a" role="img" aria-label="Dark photo of keys and documents on a desk"/>
  </svg>

  <div class="service-icon" style="left:233px;top:86px">
    <svg width="60" height="60" viewBox="0 0 60 60" fill="none" stroke="#222" stroke-width="2.4" stroke-linejoin="round">
      <path d="M34 8 L52 8 L52 26 L26 52 L8 34 Z"/>
      <circle cx="44" cy="16" r="3.5"/>
      <line x1="20" y1="34" x2="26" y2="40"/>
      <line x1="25" y1="30" x2="29" y2="34"/>
    </svg>
  </div>
  <h3 class="service-title" style="left:78px;top:234px;color:#3d3d3d">SALES</h3>
  <p class="service-copy" style="left:86px;top:277px;color:#4a4a4a">It long established fact that a reader will be distracted by the readable content of a page when looking at its layout. The point of using Lorem Ipsum is that it has a &nbsp;distribut reader will &nbsp;fact of letters, as opposed</p>
  <span class="btn-pill" style="left:220px;top:403px;background:#333;color:#fff">READ MORE</span>

  <div class="service-icon" style="left:850px;top:35px">
    <svg width="66" height="60" viewBox="0 0 66 60" fill="none" stroke="#222" stroke-width="2.6" stroke-linejoin="round">
      <path d="M6 30 L24 14 L42 30"/>
      <path d="M11 26 L11 50 L37 50 L37 26"/>
      <rect x="20" y="36" width="9" height="14"/>
      <circle cx="40" cy="14" r="8"/>
      <path d="M46 19 L60 33 L56 37 L53 34 L50 37 L45 32"/>
    </svg>
  </div>
  <h3 class="service-title" style="left:694px;top:183px;color:#fff">RENTALS</h3>
  <p class="service-copy" style="left:702px;top:226px;color:#eeeeee">It long established fact that a reader will be distracted by the readable content of a page when looking at its layout. The point of using Lorem Ipsum is that it has a &nbsp;distribut reader will &nbsp;fact of letters, as opposed</p>
  <span class="btn-pill" style="left:837px;top:351px;background:var(--brand);color:#333">READ MORE</span>
</section>

<section class="blog">
  <h2 class="section-title" style="top:2034px">LATEST BLOG</h2>
  <div class="title-rule" style="top:2099px"></div>

  <article class="post-card" style="left:111px">
    <div class="post-photo" role="img" aria-label="Photo of an agent showing a house model to a smiling couple" style="background:linear-gradient(160deg,#d9dde2 0%,#9a8f88 55%,#3e3a38 100%)"></div>
    <div class="post-body">
      <h4 class="post-title">The point of using Lorem Ips um is that it has a more</h4>
      <div class="post-meta">
        <svg width="11" height="11" viewBox="0 0 12 12" fill="#999"><circle cx="6" cy="3.5" r="3"/><path d="M0 12 Q6 4 12 12Z"/></svg>By dummy Name &nbsp;|
        <svg width="11" height="11" viewBox="0 0 12 12" fill="none" stroke="#999" stroke-width="1.3"><rect x="1" y="2" width="10" height="9"/><line x1="1" y1="5" x2="11" y2="5"/></svg>Mar 19,2021
      </div>
      <p class="post-excerpt">The point of using Lorem Ipsum is that it has a more-or-less nor mal distribution of letters, as opposed to using 'Content here, content look like readable English.</p>
    </div>
  </article>

  <article class="post-card" style="left:615px">
    <div class="post-photo" role="img" aria-label="Photo of a couple sitting together at a table in a bright office" style="background:linear-gradient(160deg,#d7c3a8 0%,#a88c6c 50%,#6a5848 100%)"></div>
    <div class="post-body">
      <h4 class="post-title">The point of using Lorem Ips um is that it has a more</h4>
      <div class="post-meta">
        <svg width="11" height="11" viewBox="0 0 12 12" fill="#999"><circle cx="6" cy="3.5" r="3"/><path d="M0 12 Q6 4 12 12Z"/></svg>By dummy Name &nbsp;|
        <svg width="11" height="11" viewBox="0 0 12 12" fill="none" stroke="#999" stroke-width="1.3"><rect x="1" y="2" width="10" height="9"/><line x1="1" y1="5" x2="11" y2="5"/></svg>Mar 19,2021
      </div>
      <p class="post-excerpt">The point of using Lorem Ipsum is that it has a more-or-less nor mal distribution of letters, as opposed to using 'Content here, content look like readable English.</p>
    </div>
  </article>
</section>

<section class="working" role="img" aria-label="Light timber floor background">
  <div class="working-visual" role="img" aria-label="Photo of hands typing on a laptop showing a row of brick houses"></div>
  <h2 class="working-title">WORKING WITH US</h2>
  <p class="working-copy">The point of using Lorem Ipsum is that it has a more-or-less normal distribution of letters, as opposed to using 'Content here</p>
  <span class="btn-cream">CLICK HERE</span>
</section>

<footer class="site-footer">
  <div class="footer-brand"><span class="brand-name">BRACKWELL</span><span class="brand-sub">REALTY</span></div>

  <h5 class="footer-heading" style="left:480px">MENU</h5>
  <ul class="footer-menu">
    <li>HOME</li><li>SALES</li><li>RENTALS</li><li>INSIGHTS</li><li>ABOUT US</li><li>WORKING WITH US</li>
  </ul>

  <h5 class="footer-heading" style="left:682px">CONTACT</h5>
  <div class="footer-item" style="left:681px;top:113px">
    <span class="footer-dot"><svg width="10" height="12" viewBox="0 0 10 12"><path d="M5 0 A4.5 4.5 0 0 1 9.5 4.5 C9.5 8 5 12 5 12 C5 12 0.5 8 0.5 4.5 A4.5 4.5 0 0 1 5 0Z" fill="#111"/><circle cx="5" cy="4.5" r="1.6" fill="#fff"/></svg></span>
    <span>1458 Dummy Text<br>lorem, CA 91710</span>
  </div>
  <div class="footer-item" style="left:681px;top:166px">
    <span class="footer-dot"><svg width="12" height="9" viewBox="0 0 12 9"><rect width="12" height="9" fill="#111"/><path d="M0.5 0.5 L6 5 L11.5 0.5" fill="none" stroke="#fff" stroke-width="1"/></svg></span>
    <span>E mail Us<br>info@company.com</span>
  </div>

  <h5 class="footer-heading" style="left:927px">FOLLOW US</h5>
  <div class="footer-item" style="left:928px;top:113px"><span class="footer-dot"></span><span>Like us on<br>FRIENDLINE</span></div>
  <div class="footer-item" style="left:928px;top:167px"><span class="footer-dot"></span><span>Follow us on<br>CHIRPNET</span></div>
  <div class="footer-item" style="left:928px;top:222px"><span class="footer-dot"></span><span>Follow us on<br>WORKLINK</span></div>

  <div class="footer-rule"></div>
  <p class="copyright">Copyright © 2021 All Rights Reserved</p>
</footer>

</body>
</html>
```